Have Logo - Need Business Card Design!!!

I am looking for a business card design for a real estate development business. The company name is Wrenfield Realty Partners. I already have a logo created by Artisan Hive and would like this logo to be incorporated into the design. I have uploaded the files. The card needs to be professional, but visually interesting. Not necessary to be double-sided, but if you want to get creative and can think of something to put on the back then have at it.

Target Market(s)

The target audience for these business cards will be professionals in the real estate industry.

Industry/Entity Type

Real Estate

Requirements
Must have
• The business card must have all the necessary items for a business card, i.e. company name, our logo, name (however, not title necessary), office address, office phone number, cell number, fax number, website address, etc.

You can use the information below for the card:

Gregory L. Danforth
718 Ridgemont Avenue
San Francisco, California 94382

www.wrenfieldrealty.example
gdanforth@wrenfieldrealty.example
Office: 415-555-0143
Fax: 415-555-0147
Cell: 415-555-0186

```html
<!DOCTYPE html>
<html lang="en">
<head>
<meta charset="utf-8">
<title>Wrenfield Realty Partners — Business Cards</title>
<link rel="stylesheet" href="https://fonts.googleapis.com/css2?family=Arimo:wght@400;700&display=swap">
<style>
  :root {
    --backdrop: #cfcfcf;
    --paper: #ffffff;
    --brand-green: #1f8a3f;
    --brand-navy: #263c7c;
    --slate: #676767;
    --ink: #1f2f6e;
    --white: #ffffff;
    --faint: rgba(31, 138, 63, 0.07);
  }
  * { box-sizing: border-box; margin: 0; padding: 0; }
  html, body {
    width: 1200px;
    height: 900px;
    overflow: hidden;
  }
  body {
    background: var(--backdrop);
    font-family: "Arimo", Arial, sans-serif;
    position: relative;
  }
  .card {
    position: absolute;
    width: 500px;
    height: 286px;
    overflow: hidden;
    box-shadow: 0 6px 14px rgba(0, 0, 0, 0.25);
  }
  .card--front { left: 70px;  top: 130px; background: var(--paper); }
  .card--slate { left: 630px; top: 130px; background: var(--slate); }
  .card--green { left: 70px;  top: 490px; background: var(--brand-green); }
  .card--navy  { left: 630px; top: 490px; background: var(--brand-navy); }

  .brand {
    display: flex;
    align-items: center;
    gap: 10px;
    font-weight: 700;
    font-size: 26px;
    letter-spacing: 0.02em;
    line-height: 1;
    white-space: nowrap;
  }
  .brand__mark {
    width: 30px;
    height: 30px;
    flex: none;
  }
  .card--front .brand { position: absolute; left: 34px; top: 36px; color: var(--brand-green); z-index: 1; }
  .card--front .brand__mark { background: var(--brand-navy); }

  .card--slate .brand { color: var(--brand-green); }
  .card--slate .brand__mark { background: var(--brand-navy); }
  .card--green .brand, .card--navy .brand { color: var(--white); }
  .card--green .brand__mark, .card--navy .brand__mark { background: var(--white); }

  .back-layout {
    position: absolute;
    inset: 0;
    display: flex;
    flex-direction: column;
    align-items: center;
    justify-content: center;
    gap: 34px;
    padding-bottom: 10px;
  }
  .website {
    font-size: 15px;
    color: var(--white);
  }

  .decor-block {
    position: absolute;
    right: 120px;
    top: 78px;
    width: 120px;
    height: 120px;
    background: var(--faint);
    z-index: 0;
  }
  .holder-name {
    position: absolute;
    left: 34px;
    top: 150px;
    font-size: 16px;
    color: var(--ink);
    z-index: 1;
  }
  .contact {
    position: absolute;
    font-size: 13.5px;
    line-height: 1.38;
    color: var(--ink);
    z-index: 1;
  }
  .contact--personal { left: 34px; top: 200px; }
  .contact--office { right: 28px; top: 146px; text-align: right; }

  .edge-stripe {
    position: absolute;
    left: 0;
    right: 0;
    bottom: 0;
    height: 9px;
    display: flex;
  }
  .edge-stripe span { height: 100%; }
  .edge-stripe .g { background: var(--brand-green); }
  .edge-stripe .n { background: var(--brand-navy); }
</style>
</head>
<body>

  <section class="card card--front" aria-label="Business card front">
    <div class="brand"><span class="brand__mark"></span>Wrenfield Realty Partners</div>
    <div class="decor-block" aria-hidden="true"></div>
    <p class="holder-name">Gregory L. Danforth</p>
    <p class="contact contact--personal">
      gdanforth@wrenfieldrealty.example<br>
      Cell: 415-555-0186
    </p>
    <p class="contact contact--office">
      718 Ridgemont Avenue<br>
      San Francisco, California 94382<br>
      Office: 415-555-0143<br>
      Fax: 415-555-0147<br>
      www.wrenfieldrealty.example
    </p>
    <div class="edge-stripe" aria-hidden="true">
      <span class="g" style="width:12%"></span>
      <span class="n" style="width:20%"></span>
      <span class="g" style="width:8%"></span>
      <span class="n" style="width:22%"></span>
      <span class="g" style="width:10%"></span>
      <span class="n" style="width:14%"></span>
      <span class="g" style="width:14%"></span>
    </div>
  </section>

  <section class="card card--slate" aria-label="Business card back, slate">
    <div class="back-layout">
      <div class="brand"><span class="brand__mark"></span>Wrenfield Realty Partners</div>
      <p class="website">www.wrenfieldrealty.example</p>
    </div>
  </section>

  <section class="card card--green" aria-label="Business card back, green">
    <div class="back-layout">
      <div class="brand"><span class="brand__mark"></span>Wrenfield Realty Partners</div>
      <p class="website">www.wrenfieldrealty.example</p>
    </div>
  </section>

  <section class="card card--navy" aria-label="Business card back, navy">
    <div class="back-layout">
      <div class="brand"><span class="brand__mark"></span>Wrenfield Realty Partners</div>
      <p class="website">www.wrenfieldrealty.example</p>
    </div>
  </section>

</body>
</html>
```